Business letterhead and powerpoint template

Hi, I have recently started using a new logo (found through MarkVesta) and would now like to use that logo for letterheads and powerpoint.

Attached is the logo and one version of a brochure I have recently used.

Business

```html
<!DOCTYPE html>
<html lang="en">
<head>
<meta charset="utf-8">
<title>Calder Capital – Presentation Template</title>
<link href="https://fonts.googleapis.com/css2?family=Jost:wght@300;400;600&family=Open+Sans:wght@600&family=Tinos:wght@700&display=swap" rel="stylesheet">
<style>
  :root {
    --canvas: #f4ebea;
    --paper: #ffffff;
    --brand-red: #e24c35;
    --ink: #1d1d1d;
    --grey-text: #8a8a8a;
    --body-grey: #6f6f6f;
    --rule: #b9b9b9;
    --scene-grey: #a7a8ad;
    --scene-orange: #ef5a24;
    --scene-red: #e5222c;
  }
  * { margin: 0; padding: 0; box-sizing: border-box; }
  html, body { width: 1200px; height: 1000px; overflow: hidden; background: var(--canvas); }
  body { position: relative; font-family: "Jost", sans-serif; }

  .slide { position: absolute; background: var(--paper); overflow: hidden; }
  .slide--cover   { left: 20px;  top: 57px;  width: 563px; height: 422px; }
  .slide--about   { left: 611px; top: 57px;  width: 570px; height: 422px; }
  .slide--services{ left: 20px;  top: 521px; width: 567px; height: 425px; }
  .slide--contact { left: 616px; top: 521px; width: 565px; height: 425px; }

  .wordmark {
    font-family: "Jost", sans-serif; font-weight: 300; color: var(--ink);
    letter-spacing: 2px; line-height: 1; text-align: center;
  }
  .wordmark small { display: block; font-size: 0.36em; letter-spacing: 4px; margin-top: 4px; }

  .cover-scene {
    position: absolute; left: 8px; top: 30px; width: 548px; height: 215px;
    background: linear-gradient(90deg, var(--scene-grey) 0 28%, var(--scene-orange) 28% 46%, var(--scene-red) 46% 64%, var(--ink) 64% 100%);
    opacity: 0.85;
  }
  .cover-wordmark { position: absolute; left: 52px; top: 262px; width: 275px; font-size: 48px; }
  .cover-wordmark small { border-top: 1px solid var(--rule); padding-top: 4px; }
  .cover-url {
    position: absolute; left: 75px; top: 345px;
    font-family: "Open Sans", sans-serif; font-weight: 600; font-size: 16px; color: var(--ink);
  }

  .slide-header {
    position: absolute; left: 0; top: 0; width: 100%; height: 46px; background: var(--paper);
    box-shadow: 0 4px 6px rgba(0,0,0,0.22);
    display: flex; align-items: center; justify-content: space-between; padding: 0 18px 0 10px;
  }
  .slide-header .wordmark { font-size: 22px; text-align: left; }
  .slide-header .wordmark small { font-size: 8px; letter-spacing: 3px; margin-top: 1px; }
  .slide-title { font-family: "Jost", sans-serif; font-weight: 400; font-size: 21px; color: var(--grey-text); letter-spacing: 1px; }

  .slide-body {
    position: absolute; font-family: "Tinos", serif; font-weight: 700; font-size: 11.5px;
    color: var(--body-grey); line-height: 1.42; text-shadow: 1px 1px 1px rgba(0,0,0,0.15);
  }
  .slide--about .slide-body { left: 20px; top: 154px; width: 530px; }
  .slide-body ol { margin: 10px 0 0 22px; }
  .slide--services .slide-body { left: 122px; top: 146px; width: 400px; }
  .slide-body ul { list-style: none; margin: 14px 0 0 18px; }
  .slide-body ul li { margin-bottom: 11px; }
  .slide-body ul li::before { content: "▪ "; font-size: 9px; }

  .footer-band { position: absolute; left: 0; bottom: 0; height: 29px; background: var(--brand-red); }
  .slide--about .footer-band { width: 504px; }
  .slide--services .footer-band { width: 503px; }
  .footer-mark { position: absolute; right: 12px; bottom: 4px; width: 26px; height: 26px; background: var(--brand-red); }

  .contact-heading {
    position: absolute; left: 0; top: 48px; width: 100%; text-align: center;
    font-weight: 600; font-size: 35px; color: var(--brand-red);
  }
  .contact-band { position: absolute; left: 0; top: 104px; width: 100%; height: 212px; background: var(--brand-red); }
  .contact-band .wordmark { position: absolute; left: 192px; top: 42px; width: 180px; font-size: 32px; color: var(--paper); }
  .contact-band .wordmark small { border-top: 1px solid rgba(255,255,255,0.6); font-size: 11px; }
  .contact-details { position: absolute; left: 222px; top: 110px; list-style: none; color: var(--paper); font-size: 8.5px; line-height: 1.35; }
  .contact-details li { position: relative; padding-left: 15px; }
  .contact-details svg { position: absolute; left: 0; top: 1px; }
  .contact-details .gap { margin-top: 3px; }
</style>
</head>
<body>

<section class="slide slide--cover">
  <div class="cover-scene" role="img" aria-label="Illustration of four coloured tower blocks with trees on a road"></div>
  <div class="wordmark cover-wordmark">CALDER<small>CAPITAL</small></div>
  <p class="cover-url">www.caldercapital.com.au</p>
</section>

<section class="slide slide--about">
  <header class="slide-header">
    <div class="wordmark">CALDER<small>CAPITAL</small></div>
    <h2 class="slide-title">About us</h2>
  </header>
  <div class="slide-body">
    <p>Calder Capital is a real estate focused group formed in 2008 to do two things:</p>
    <ol>
      <li>Undertake select real estate advisory services to real estate investors who own or have the desire to own Australian real estate.</li>
      <li>Assist leading real estate investors and managers to raise institutional capital from the Asia Pacific region.</li>
    </ol>
  </div>
  <div class="footer-band"></div>
  <div class="footer-mark"></div>
</section>

<section class="slide slide--services">
  <header class="slide-header">
    <div class="wordmark">CALDER<small>CAPITAL</small></div>
    <h2 class="slide-title">Services</h2>
  </header>
  <div class="slide-body">
    <p>Major services under Calder Capital portfolio are :</p>
    <ul>
      <li>Australian Real Estate Advisory Services</li>
      <li>Institutional Capital Raising</li>
    </ul>
  </div>
  <div class="footer-band"></div>
  <div class="footer-mark"></div>
</section>

<section class="slide slide--contact">
  <h2 class="contact-heading">Get in Touch</h2>
  <div class="contact-band">
    <div class="wordmark">CALDER<small>CAPITAL</small></div>
    <ul class="contact-details">
      <li><svg width="8" height="10" viewBox="0 0 8 10"><path d="M4 0a4 4 0 0 0-4 4c0 3 4 6 4 6s4-3 4-6a4 4 0 0 0-4-4zm0 5.5a1.5 1.5 0 1 1 0-3 1.5 1.5 0 0 1 0 3z" fill="#fff"/></svg>CALDER CAPITAL<br>Level 9 Suite 14<br>48 Ridge Lane<br>Northbank 2100 NSW<br>Australia</li>
      <li class="gap"><svg width="8" height="10" viewBox="0 0 8 10"><rect x="1" y="0" width="6" height="10" rx="1" fill="#fff"/><rect x="2" y="1.5" width="4" height="5" fill="#e24c35"/></svg>Phone:&nbsp; +61 (0)2 9000 4172</li>
      <li><svg width="10" height="9" viewBox="0 0 10 9"><rect x="2" y="0" width="6" height="3" fill="#fff"/><rect x="0" y="3" width="10" height="4" rx="1" fill="#fff"/><rect x="2" y="6" width="6" height="3" fill="#fff"/></svg>Fax:&nbsp;&nbsp;&nbsp;&nbsp;&nbsp; +61 (0)2 9000 4180</li>
      <li><svg width="9" height="9" viewBox="0 0 9 9"><circle cx="4.5" cy="4.5" r="4" fill="none" stroke="#fff"/><path d="M0.5 4.5h8M4.5 0.5c-2 2.5-2 5.5 0 8M4.5 0.5c2 2.5 2 5.5 0 8" stroke="#fff" fill="none" stroke-width="0.7"/></svg>www.caldercapital.com.au</li>
    </ul>
  </div>
</section>

</body>
</html>
```